PackAndRoamCrew Graphic Designer Search

We need a skilled Graphic Designer to continue work on our Website. Currently, we are looking to create Infographic Pages for each country/city we visit/travel to. Currently, we are looking for Thailand, China, Bali, Italy, and Egypt. A Sample of Puerto Rico is attached.
In a SIMILAR design format and style, we would need the following:
* MAP for Thailand, China, Bali, and Italy, Egypt, Sweden, Curacao, St. Lucia, St Thomas, Jamaica.
* Country-specific Icons for the "Top Experiences" Section (i.e Pandas, Temples, Museums.
* Flag of the country

Later we will need caricature modifications/updates as well. (added samples to see the type of flow we are looking for)

We would like to see adaptations to the example attached or your own idea based on the look and feel of the page we provided to you.

Formats in Illustrator of Photoshop preferred (full layers should be able to modify aspects of the map and icons

Target Market(s)

Travel/Tourism

Industry/Entity Type

Travel

Colors
0054AA
0677BA
7BADD7
CADEEF
E8F1F8
0094D4
00A9DD
6FCCEA
C7EBF8
E9F6FB
FFF300
FFF600
FEFA6F
FFFEC7
FFFEE8
F0912C
F2A743
F7CA91
FBE8D2
FDF5EE
EE7325
F08F49
F5BC92
FAE3D3
FDF4ED

Requirements
Must have
• talent
Nice to have
• talent

```html
<!DOCTYPE html>
<html lang="en">
<head>
<meta charset="utf-8">
<title>China – Infographic Travel Guide</title>
<link href="https://fonts.googleapis.com/css2?family=Titan+One&family=Oswald:wght@300;400;600&display=swap" rel="stylesheet">
<style>
  :root{
    --navy:#1f1a6b;
    --orange:#F0912C;
    --orange-deep:#EE7325;
    --sky:#00A9DD;
    --cyan:#17e4f7;
    --land:#b5cf4a;
    --red:#ff2a0e;
    --yellow:#FFF300;
    --pale-blue:#CADEEF;
    --mid-blue:#7BADD7;
    --white:#ffffff;
  }
  *{box-sizing:border-box;margin:0;padding:0}
  html,body{width:1176px;height:1200px;overflow:hidden;background:var(--white)}
  .guide{position:relative;width:1176px;height:1200px;font-family:"Oswald",sans-serif}
  .brand{position:absolute;left:52px;top:96px;display:flex;align-items:center;gap:8px}
  .brand-dot{width:22px;height:22px;border-radius:50%;background:var(--orange)}
  .brand-name{font-family:"Oswald",sans-serif;font-weight:600;font-size:22px;color:var(--navy)}
  .title{position:absolute;left:327px;width:516px;top:44px;text-align:center;
    font-family:"Titan One",sans-serif;font-size:74px;line-height:1;color:var(--navy);letter-spacing:1px}
  .ribbon{position:absolute;left:262px;top:142px;width:646px;height:76px}
  .ribbon-text{position:absolute;left:327px;top:142px;width:516px;height:49px;
    display:flex;align-items:center;justify-content:center;
    font-family:"Oswald",sans-serif;font-weight:600;font-size:33px;color:var(--white);letter-spacing:1.5px}
  .flag{position:absolute;left:934px;top:61px;width:204px;height:137px}
  .flight-path{position:absolute;left:79px;top:280px;width:250px;height:8px}
  .map{position:absolute;left:62px;top:228px;width:1070px;height:524px}
  .facts{position:absolute;inset:0;pointer-events:none}
  .fact-icon{position:absolute;width:113px;height:113px}
  .fact-label{position:absolute;font-weight:300;font-size:22px;color:var(--orange);line-height:1}
  .fact-value{position:absolute;font-weight:600;color:var(--orange);line-height:1.08;letter-spacing:.5px}
  .v-lg{font-size:38px}
  .v-md{font-size:26px}
  .v-cl{font-size:29px}
  .baseline{position:absolute;left:0;bottom:0;width:1176px;height:2px;background:var(--orange)}
</style>
</head>
<body>
<main class="guide">

  <div class="brand"><span class="brand-dot"></span><span class="brand-name">PackAndRoamCrew</span></div>

  <h1 class="title">CHINA</h1>

  <svg class="ribbon" viewBox="0 0 646 76" aria-hidden="true">
    <polygon points="0,22 65,22 65,76 0,76 30,49" fill="var(--orange)" stroke="var(--navy)" stroke-width="3"/>
    <polygon points="646,22 581,22 581,76 646,76 616,49" fill="var(--orange)" stroke="var(--navy)" stroke-width="3"/>
    <polygon points="65,49 99,76 65,76" fill="var(--orange-deep)" stroke="var(--navy)" stroke-width="3"/>
    <polygon points="581,49 547,76 581,76" fill="var(--orange-deep)" stroke="var(--navy)" stroke-width="3"/>
    <rect x="65" y="1.5" width="516" height="48" fill="var(--orange)" stroke="var(--navy)" stroke-width="3"/>
  </svg>
  <div class="ribbon-text">INFOGRAPHIC TRAVEL GUIDE</div>

  <svg class="flag" viewBox="0 0 204 137" role="img" aria-label="Flag of China">
    <rect x="2" y="2" width="200" height="133" fill="var(--red)" stroke="var(--navy)" stroke-width="4"/>
    <polygon points="34,18 39,33 55,33 42,42 47,57 34,48 21,57 26,42 13,33 29,33" fill="var(--yellow)"/>
    <polygon points="66,12 68,17 73,17 69,20 71,25 66,22 61,25 63,20 59,17 64,17" fill="var(--yellow)"/>
    <polygon points="78,25 80,30 85,30 81,33 83,38 78,35 73,38 75,33 71,30 76,30" fill="var(--yellow)"/>
    <polygon points="78,44 80,49 85,49 81,52 83,57 78,54 73,57 75,52 71,49 76,49" fill="var(--yellow)"/>
    <polygon points="66,57 68,62 73,62 69,65 71,70 66,67 61,70 63,65 59,62 64,62" fill="var(--yellow)"/>
  </svg>

  <svg class="flight-path" viewBox="0 0 250 8" aria-hidden="true">
    <line x1="0" y1="4" x2="250" y2="4" stroke="var(--sky)" stroke-width="1.5" stroke-dasharray="12 14 28 14 48 14 90 0"/>
  </svg>

  <svg class="map" viewBox="0 0 1070 524" role="img" aria-label="Illustrated map of China surrounded by sea, with pagodas, pandas, bamboo, the Great Wall, city skyline, sailing junks and a ship">
    <defs>
      <linearGradient id="mapTone" x1="0" y1="0" x2="1" y2="0">
        <stop offset="0" stop-color="var(--cyan)"/>
        <stop offset=".5" stop-color="var(--land)"/>
        <stop offset="1" stop-color="var(--cyan)"/>
      </linearGradient>
    </defs>
    <path d="M40,170 C60,120 200,110 330,95 C420,60 520,70 640,60 C700,20 760,10 820,40 C900,30 980,60 1060,110 C1080,190 1040,260 960,300 C900,330 840,380 790,470 C720,520 650,520 600,470 C500,420 440,440 360,400 C270,370 130,380 60,320 C10,280 20,220 40,170 Z" fill="url(#mapTone)"/>
  </svg>

  <section class="facts">
    <svg class="fact-icon" style="left:60px;top:638px" viewBox="0 0 113 113" aria-hidden="true">
      <polygon points="56,4 110,42 2,42" fill="var(--pale-blue)" stroke="var(--navy)" stroke-width="3"/>
      <rect x="8" y="42" width="97" height="10" fill="var(--pale-blue)" stroke="var(--navy)" stroke-width="3"/>
      <rect x="18" y="52" width="10" height="40" fill="var(--white)" stroke="var(--navy)" stroke-width="3"/>
      <rect x="85" y="52" width="10" height="40" fill="var(--white)" stroke="var(--navy)" stroke-width="3"/>
      <rect x="2" y="96" width="109" height="14" fill="var(--pale-blue)" stroke="var(--navy)" stroke-width="3"/>
      <path d="M56,100 C44,82 38,74 38,64 a18,18 0 0 1 36,0 C74,74 68,82 56,100 Z" fill="var(--red)" stroke="var(--navy)" stroke-width="3"/>
      <circle cx="56" cy="64" r="7" fill="var(--white)" stroke="var(--navy)" stroke-width="3"/>
    </svg>
    <div class="fact-label" style="left:210px;top:664px">Capital:</div>
    <div class="fact-value v-lg" style="left:210px;top:688px">SAN JUAN</div>

    <svg class="fact-icon" style="left:60px;top:767px" viewBox="0 0 113 113" aria-hidden="true">
      <g fill="var(--orange)" stroke="var(--navy)" stroke-width="3">
        <circle cx="16" cy="14" r="12"/><circle cx="56" cy="14" r="12"/><circle cx="97" cy="14" r="12"/>
        <rect x="3" y="32" width="26" height="48" rx="10"/>
        <rect x="84" y="32" width="26" height="48" rx="10"/>
        <polygon points="56,32 74,80 38,80"/>
        <rect x="12" y="78" width="8" height="33"/><rect x="93" y="78" width="8" height="33"/>
        <rect x="52" y="78" width="8" height="33"/>
      </g>
    </svg>
    <div class="fact-label" style="left:210px;top:793px">Population:</div>
    <div class="fact-value v-lg" style="left:210px;top:818px">3,706,690 (2019)</div>

    <svg class="fact-icon" style="left:60px;top:910px" viewBox="0 0 113 86" aria-hidden="true">
      <g fill="none" stroke="var(--orange)" stroke-width="4">
        <polyline points="2,22 2,2 22,2"/><polyline points="91,2 111,2 111,22"/>
        <polyline points="2,64 2,84 22,84"/><polyline points="111,64 111,84 91,84"/>
      </g>
      <path d="M56,84 C38,56 30,44 30,30 a26,26 0 0 1 52,0 C82,44 74,56 56,84 Z" fill="var(--red)" stroke="var(--navy)" stroke-width="3"/>
      <circle cx="56" cy="30" r="11" fill="var(--white)" stroke="var(--navy)" stroke-width="3"/>
    </svg>
    <div class="fact-label" style="left:210px;top:905px">Area:</div>
    <div class="fact-value v-lg" style="left:210px;top:927px">3,515 sq mi<br>(9104 km2)</div>

    <svg class="fact-icon" style="left:60px;top:1024px" viewBox="0 0 113 113" aria-hidden="true">
      <polygon points="56,4 110,34 2,34" fill="var(--pale-blue)" stroke="var(--navy)" stroke-width="3"/>
      <rect x="8" y="34" width="97" height="12" fill="var(--pale-blue)" stroke="var(--navy)" stroke-width="3"/>
      <g fill="var(--white)" stroke="var(--navy)" stroke-width="3">
        <rect x="18" y="46" width="12" height="46"/><rect x="42" y="46" width="12" height="46"/>
        <rect x="62" y="46" width="12" height="46"/><rect x="84" y="46" width="12" height="46"/>
      </g>
      <rect x="2" y="94" width="109" height="16" fill="var(--pale-blue)" stroke="var(--navy)" stroke-width="3"/>
    </svg>
    <div class="fact-label" style="left:210px;top:1032px">Government:</div>
    <div class="fact-value v-md" style="left:210px;top:1055px">CARIBBEAN ISLAND -<br>UNINCORPORATED<br>US TERRITORY</div>

    <svg class="fact-icon" style="left:658px;top:767px" viewBox="0 0 113 113" aria-hidden="true">
      <rect x="2" y="38" width="108" height="12" rx="6" fill="var(--mid-blue)"/>
      <rect x="2" y="68" width="108" height="12" rx="6" fill="var(--mid-blue)"/>
      <rect x="24" y="2" width="66" height="109" rx="7" fill="var(--pale-blue)" stroke="var(--navy)" stroke-width="3"/>
      <line x1="50" y1="10" x2="64" y2="10" stroke="var(--navy)" stroke-width="3" stroke-linecap="round"/>
      <circle cx="57" cy="102" r="4" fill="none" stroke="var(--navy)" stroke-width="2"/>
      <g stroke="var(--orange)" stroke-width="5" stroke-linecap="round">
        <line x1="52" y1="40" x2="44" y2="76"/><line x1="68" y1="40" x2="60" y2="76"/>
        <line x1="40" y1="52" x2="74" y2="52"/><line x1="38" y1="64" x2="72" y2="64"/>
      </g>
    </svg>
    <div class="fact-label" style="left:806px;top:795px">Country code:</div>
    <div class="fact-value v-lg" style="left:806px;top:818px">001</div>

    <svg class="fact-icon" style="left:658px;top:910px" viewBox="0 0 113 86" aria-hidden="true">
      <g fill="none" stroke="var(--orange)" stroke-width="3">
        <circle cx="42" cy="43" r="40"/><ellipse cx="42" cy="43" rx="18" ry="40"/>
        <line x1="2" y1="43" x2="82" y2="43"/><line x1="42" y1="3" x2="42" y2="83"/>
      </g>
      <rect x="54" y="24" width="56" height="60" rx="8" fill="var(--red)" stroke="var(--navy)" stroke-width="3"/>
      <circle cx="82" cy="54" r="21" fill="var(--white)" stroke="var(--navy)" stroke-width="3"/>
      <polyline points="82,40 82,54 92,60" fill="none" stroke="var(--navy)" stroke-width="3" stroke-linecap="round"/>
    </svg>
    <div class="fact-label" style="left:806px;top:916px">Timezone:</div>
    <div class="fact-value v-md" style="left:806px;top:939px">ATLANTIC STANDARD<br>TIME (UTC-4)</div>

    <svg class="fact-icon" style="left:658px;top:1024px" viewBox="0 0 113 113" aria-hidden="true">
      <g stroke="var(--orange)" stroke-width="5" stroke-linecap="round">
        <line x1="52" y1="2" x2="52" y2="18"/><line x1="4" y1="50" x2="20" y2="50"/>
        <line x1="84" y1="50" x2="100" y2="50"/><line x1="18" y1="16" x2="28" y2="26"/>
        <line x1="86" y1="16" x2="76" y2="26"/><line x1="18" y1="84" x2="28" y2="74"/>
      </g>
      <circle cx="52" cy="50" r="24" fill="var(--yellow)" stroke="var(--orange)" stroke-width="3"/>
      <path d="M54,110 h44 a14,14 0 0 0 0,-28 a20,20 0 0 0 -38,-4 a16,16 0 0 0 -6,32 Z" fill="var(--pale-blue)" stroke="var(--mid-blue)" stroke-width="3"/>
    </svg>
    <div class="fact-label" style="left:806px;top:1035px">Climate:</div>
    <div class="fact-value v-cl" style="left:806px;top:1056px">TROPICAL<br>RAINFOREST</div>
  </section>

  <div class="baseline"></div>
</main>
</body>
</html>
```